Soap box for artisan soaps, eco-look, high design

We need a soap box for our lovely artisan soaps. The box size is: 9 cm height x 6,5 cm width x 2,8 cm depth. It would be nice when there is a small window in the box so you can see the soap.

See attachment for an example soap box (upside down). Please use the same elements such as texts and industrie logos. The idea is that we have a generic design that we can custom-made for different soaps. We have 15 different soaps in total at the moment.

Target Market(s)

Middle to high income

Font styles to use
Decorative
Script

Requirements
Must have
• Dutch text:
• Etherische oliën
• Handgemaakt
• Natuurlijke ingrediënten

```html
<!DOCTYPE html>
<html lang="nl">
<head>
<meta charset="utf-8">
<title>Velora – Lemon and Poppy zeepdoos</title>
<link href="https://fonts.googleapis.com/css2?family=Abril+Fatface&family=Great+Vibes&family=Raleway:wght@400;500;700&family=Montserrat:wght@700&display=swap" rel="stylesheet">
<style>
  :root{
    --kraft:#c9a47a;
    --leaf:#c8902c;
    --cut:#111111;
    --fold:#e0301e;
    --frame:#d48a22;
    --accent-blue:#0e4263;
    --ink:#1a1510;
    --paper:#ffffff;
  }
  *{box-sizing:border-box;margin:0;padding:0}
  html,body{width:1094px;height:1200px;overflow:hidden;background:var(--paper)}
  .sheet{position:relative;width:1094px;height:1200px}
  .kraft{position:absolute;left:12px;top:8px;width:1070px;height:1180px;background:var(--kraft)}
  .leaf-pattern{position:absolute;opacity:.55}
  .leaf-pattern.top{left:30px;top:10px;width:1040px;height:610px;
    background:radial-gradient(ellipse at 15% 40%,var(--leaf) 0%,transparent 45%),
               radial-gradient(ellipse at 85% 40%,var(--leaf) 0%,transparent 45%),
               radial-gradient(ellipse at 50% 5%,var(--leaf) 0%,transparent 40%);}
  .leaf-pattern.front{left:620px;top:860px;width:190px;height:145px;
    background:radial-gradient(ellipse at 80% 70%,var(--leaf) 0%,transparent 65%);}
  .dieline{position:absolute;left:0;top:0;width:1094px;height:1200px}
  .panel{position:absolute;color:var(--ink);font-family:"Raleway",sans-serif}
  .flipped{transform:rotate(180deg)}
  .brand-name{font-family:"Raleway",sans-serif;font-weight:700;color:var(--ink);letter-spacing:.5px}

  /* back panel */
  .back{left:286px;top:88px;width:522px;height:380px}
  .back .story{position:absolute;left:29px;top:40px;width:272px}
  .story h2{font-family:"Abril Fatface",serif;font-weight:400;font-size:23px;margin-bottom:14px}
  .story p{font-size:11.3px;line-height:19.6px;text-align:justify}
  .signature{position:absolute;left:22px;top:298px;font-family:"Great Vibes",cursive;font-size:48px;white-space:nowrap}
  .free-of{position:absolute;left:335px;top:29px;width:160px;height:131px;border:1px solid var(--ink);padding:12px 14px;font-size:11px;line-height:16px}
  .free-of h3{font-family:"Abril Fatface",serif;font-weight:400;font-size:17px;margin-bottom:4px}
  .back .brand-name{position:absolute;left:335px;top:190px;width:160px;font-size:34px;text-align:center}
  .address{position:absolute;left:338px;top:247px;font-size:9px}
  .url{position:absolute;left:338px;top:262px;font-family:"Abril Fatface",serif;font-size:13px}
  .weight{position:absolute;left:338px;top:310px;display:flex;align-items:center;gap:12px;font-family:"Abril Fatface",serif;font-size:20px}
  .weight svg{display:block}

  /* ingredients panel */
  .ingredients{left:286px;top:468px;width:522px;height:161px}
  .ingredients p{position:absolute;left:45px;top:46px;width:430px;font-size:10.3px;line-height:16.4px;text-align:justify}
  .ingredients strong{font-weight:700}

  /* front panel */
  .front{left:286px;top:629px;width:522px;height:378px}
  .frame{position:absolute;left:55px;top:71px;width:417px;height:254px;border:2.5px solid var(--frame)}
  .soap-window{position:absolute;left:86px;top:31px;width:351px;height:87px;
    background:linear-gradient(90deg,#e9b08a 0%,#dba078 30%,#e09a3c 45%,#d88a2a 70%,#e2a246 100%)}
  .accent-square{position:absolute;left:231px;top:66px;width:60px;height:60px;background:var(--accent-blue)}
  .front .brand-name{position:absolute;left:0;top:136px;width:522px;text-align:center;font-size:22px}
  .product-name{position:absolute;left:0;top:186px;width:522px;text-align:center;font-family:"Great Vibes",cursive;font-size:58px;white-space:nowrap}
  .product-type{position:absolute;left:0;top:288px;width:522px;text-align:center;font-family:"Montserrat",sans-serif;font-weight:700;font-size:17px;letter-spacing:.5px}
  .tagline{position:absolute;left:0;top:334px;width:522px;text-align:center;font-size:15px;font-weight:500}

  /* bottom panel */
  .bottom{left:286px;top:1007px;width:522px;height:161px}
  .bottom p{position:absolute;left:47px;top:32px;width:275px;font-size:11.6px;line-height:16.6px}
  .bottom .brand-name{position:absolute;left:358px;top:92px;font-size:36px}
</style>
</head>
<body>
<div class="sheet">
  <div class="kraft"></div>
  <div class="leaf-pattern top" role="img" aria-label="Decoratief patroon van ranken en bladeren"></div>
  <div class="leaf-pattern front" role="img" aria-label="Decoratief patroon van ranken en bladeren"></div>

  <svg class="dieline" viewBox="0 0 1094 1200" fill="none">
    <g stroke="var(--cut)" stroke-width="1.8">
      <path d="M286 88 L304 24 H790 L808 88"/>
      <path d="M286 88 H121 V98 Q55 98 31 150 V410 Q55 458 121 458 V468 H286"/>
      <path d="M808 88 H974 V98 Q1040 98 1064 150 V410 Q1040 458 974 458 V468 H808"/>
      <path d="M121 98 V124 H148 M121 458 V433 H148"/>
      <path d="M974 98 V124 H947 M974 458 V433 H947"/>
      <path d="M286 468 L137 492 L135 584 L286 629"/>
      <path d="M808 468 L958 492 L960 584 L808 629"/>
      <path d="M286 629 V1007 M808 629 V1007"/>
      <path d="M286 1007 L135 1047 V1139 L286 1168 H808 L960 1139 V1047 L808 1007"/>
    </g>
    <g stroke="var(--fold)" stroke-width="1.6">
      <path d="M286 88 H808 M286 468 H808 M286 629 H808 M286 1007 H808"/>
      <path d="M286 88 V1168 M808 88 V1168"/>
      <path d="M124 124 V433 M971 124 V433"/>
    </g>
  </svg>

  <section class="panel back flipped">
    <div class="story">
      <h2>Onze zeep</h2>
      <p>Het geeft jouw huid een heerlijk gevoel met zachte bubbels en rijke geur! Handgemaakt in kleine batches met eerlijke ingrediënten en essentiële oliën. Elke zeep wordt alleen geproduceerd als het iets goeds voor je doet en droogt minstens zes weken voordat ze worden verpakt. Ze zien er te mooi uit om te openen, maar hoe ga je dan genieten van de heerlijke bubbels, de ongelooflijke geur en je zachte, zijdeachtige huid?</p>
    </div>
    <div class="signature">Lina Veldkamp</div>
    <div class="free-of">
      <h3>Vrij van:</h3>
      SLA &amp; SLSA<br>Alcohol &amp; Parabenen<br>Sobaten &amp; Siliconen<br>Sulfaat &amp; Conserverings-<br>middelen
    </div>
    <div class="brand-name">Velora</div>
    <div class="address">Oosthaven, Nederland</div>
    <div class="url">velora.nl</div>
    <div class="weight">
      <span>120g ℮</span>
      <svg width="30" height="30" viewBox="0 0 30 30"><circle cx="15" cy="15" r="14" fill="var(--ink)"/></svg>
      <svg width="30" height="30" viewBox="0 0 30 30" fill="none" stroke="var(--ink)" stroke-width="2"><rect x="3" y="5" width="24" height="8" rx="4"/><rect x="3" y="13" width="24" height="13" rx="5"/></svg>
    </div>
  </section>

  <section class="panel ingredients flipped">
    <p><strong>Ingrediënts:</strong> Olijf olie pomace (Olea europaea), Kokosnoot olie (Cocos nucifera), Palm olie (Elaeis Guineensis Kernel Oil), Water (Aqua), Citroen Etherische Olie (Citrus limonum), maanzaad (Papaver somniferum), ijzer oxide geel (Iron Oxide). Natuurlijke bestanddelen van Etherische Olie – Citral, Citronellol, Geraniol, Limonene, Linalool.</p>
  </section>

  <section class="panel front">
    <div class="frame"></div>
    <div class="soap-window" role="img" aria-label="Venster met zicht op de oranje-roze citroen- en maanzaadzeep"></div>
    <div class="accent-square"></div>
    <div class="brand-name">Velora</div>
    <div class="product-name">Lemon and Poppy</div>
    <div class="product-type">ETHERISCHE ZEEP</div>
    <div class="tagline">Met liefde gemaakt</div>
  </section>

  <section class="panel bottom">
    <p>Essentiële oliën van Lemon creëren een levendige explosie van positieve goodness, waardoor u vrolijk wakker word. Poppy seeds worden toegevoegd om een beetje kracht te geven bij het exfoliëren. *Lemon helpt je in een positieve state of mind te komen, waardoor je de dag beter aan kan.</p>
    <div class="brand-name">Velora</div>
  </section>
</div>
</body>
</html>
```